Waterproofing Construction company needs letterhead

I need a letterhead design for a commercial waterproofing construction company. We would like to see designs that are contemporary, clean, sleek and use our logo. Our current design is dated. I would also like a cover page (see example) that goes with our letterhead. I would like for the footer to have our address, website, and phone number

Target Market(s)

Customers, potential customers.

Font styles to use
Sans Serif

Requirements
Must have
• logo, website, address, phone numbers, only our colors, tahoma font
• PMS: 295C PMS: 2995C
• CMYK: 100/84/36/39 CMYK: 80/12/1/0
• RGB: 16/44/82 RGB: 0/167/224
• HEX#: #102C52 HEX#: #00A7E0
• Black & White: 100% Black & White: 32%
• Gray Scale: 90% Gray Scale: 32%
Nice to have
• Our "icon" logo attached would be nice somewhere on the page.

```html
<!DOCTYPE html>
<html lang="en">
<head>
<meta charset="utf-8">
<title>Nolan Shield Letterhead</title>
<link href="https://fonts.googleapis.com/css2?family=Noto+Sans:wght@400;800&display=swap" rel="stylesheet">
<style>
  :root {
    --navy: #102C52;
    --cyan: #00A7E0;
    --backdrop: #D7DCE6;
    --paper: #FFFFFF;
    --accent-grey: #D0D0DA;
    --accent-ice: #E1EDF8;
    --ink: #1A1A1A;
  }
  * { margin: 0; padding: 0; box-sizing: border-box; }
  html, body {
    width: 1200px; height: 1200px; overflow: hidden;
    background: var(--backdrop);
    font-family: "Noto Sans", Tahoma, sans-serif;
  }
  .stage { position: relative; width: 1200px; height: 1200px; }
  .letterhead {
    position: absolute; left: 147px; top: 52px;
    width: 714px; height: 863px;
    background: var(--paper);
    transform: scale(1.27); transform-origin: 0 0;
    overflow: hidden;
  }
  .edge-bar { position: absolute; top: 0; bottom: 0; }
  .edge-bar--cyan { left: 0; width: 20px; background: var(--cyan); }
  .edge-bar--navy { left: 20px; width: 10px; background: var(--navy); }
  .brand {
    position: absolute; left: 65px; top: 28px;
    display: flex; align-items: center; gap: 8px;
  }
  .brand__mark { width: 14px; height: 14px; background: var(--cyan); }
  .brand__name {
    font-weight: 800; font-size: 30px; letter-spacing: -0.5px;
    color: var(--navy); line-height: 1;
  }
  .corner-accent { position: absolute; left: 0; top: 0; width: 714px; height: 863px; }
  .contact-tab {
    position: absolute; left: 0; top: 739px;
    width: 40px; height: 94px;
    background: var(--cyan);
    border-radius: 0 8px 8px 0;
  }
  .contact-tab svg { position: absolute; left: 17px; width: 12px; height: 12px; fill: #fff; }
  .contact-tab .icon-web { top: 12px; }
  .contact-tab .icon-pin { top: 40px; }
  .contact-tab .icon-phone { top: 67px; }
  .contact {
    position: absolute; left: 53px;
    font-size: 13px; color: var(--ink); line-height: 16px;
    white-space: nowrap;
  }
  .contact--web { top: 749px; }
  .contact--address { top: 781px; }
  .contact--phones { top: 809px; left: 50px; }
</style>
</head>
<body>
<div class="stage">
  <div class="letterhead">
    <div class="edge-bar edge-bar--cyan"></div>
    <div class="edge-bar edge-bar--navy"></div>

    <div class="brand">
      <span class="brand__name">Nolan Shield</span>
      <span class="brand__mark"></span>
    </div>

    <svg class="corner-accent" viewBox="0 0 714 863" aria-hidden="true">
      <circle cx="714" cy="863" r="300" fill="var(--accent-ice)"/>
      <circle cx="714" cy="863" r="170" fill="var(--accent-grey)"/>
    </svg>

    <div class="contact-tab">
      <svg class="icon-web" viewBox="0 0 12 12"><circle cx="6" cy="6" r="5.5"/><path d="M3 4.5 5 3.5 6 5 4.5 6.5z M7 7 9 6.5 8.5 9z" fill="var(--cyan)"/></svg>
      <svg class="icon-pin" viewBox="0 0 12 12"><path d="M6 0.5a4 4 0 0 1 4 4c0 3-4 7-4 7s-4-4-4-7a4 4 0 0 1 4-4z"/><circle cx="6" cy="4.5" r="1.5" fill="var(--cyan)"/></svg>
      <svg class="icon-phone" viewBox="0 0 12 12"><path d="M2.5 0.8 4.5 3 3.5 4.5c.8 1.6 2 2.8 3.6 3.6L8.6 7.1l2.2 2-1.2 1.9C5.5 10.7 1.2 6.4 0.8 2.2z"/></svg>
    </div>

    <p class="contact contact--web">www.nolanshield.com</p>
    <p class="contact contact--address">PO Box 417 | Cary Ridge, NC 27519</p>
    <p class="contact contact--phones">(877) 555-0142<br>(919) 555-0187</p>
  </div>
</div>
</body>
</html>
```